Varnel Psychiatry (Psychiatry clinic offering cutting edge treatments)

2 sided flyer for new psychiatry practice in Boulder, CO. I want something that looks professional, cutting edge, but also welcoming and friendly. My logo and pictures are attached.

Some of the copy:
Personalized, holistic Psychiatry combined with cutting-edge, evidence-based treatments. Our personalized psychiatry plan includes a bio-psycho-social evaluation, personalized treatment plan, medical evaluation for underlying hormonal and electrolyte abnormalities, and genetic testing (when warranted).

We specialize in treatment-resistant depression and substance abuse. We also treat PTSD, Bipolar Disorder, OCD, anxiety disorders, ADHD, and psychotic disorders.

About Dr. Brok- Dr. Brok served as Chief Resident at the largest private psychiatry hospital in Colorado. While there he won 3 consecutive awards for exceptionally high Psychiatry in service test score (99th percentile). He was a board member of Kestrel Mind Guild and helped advocate for better Colorado mental health policy. Dr. Brok is uniquely trained in Ketamine, Transcranial Magnetic Stimulation, and integrative psychiatry.

Target Market(s)

Private pay mental health patients, planning to give out to psychologists and family practice doctors

Industry/Entity Type

Medicine/Psychiatry

Colors
0054AA
0677BA
7BADD7
CADEEF
E8F1F8
0094D4
00A9DD
6FCCEA
C7EBF8
E9F6FB
00AB8E
00BBA5
67D7C9
C6EFE9
E9F9F6

Requirements
Must have
• My logo, an about me (Dr. Tomas Brok) section

```html
<!DOCTYPE html>
<html lang="en">
<head>
<meta charset="utf-8">
<title>Varnel Psychiatry – Two-Sided Flyer</title>
<link href="https://fonts.googleapis.com/css2?family=Poppins:wght@400;500;600;700;800&family=Allura&display=swap" rel="stylesheet">
<style>
  :root{
    --stage:#909195;
    --ink:#111111;
    --black:#050505;
    --white:#ffffff;
    --purple:#a63ee6;
    --violet:#6a3bd8;
    --blue:#2f5fe0;
    --cyan:#19d3f0;
    --lavender:#e4dcfb;
    --body-font:'Poppins',sans-serif;
    --script-font:'Allura',cursive;
  }
  *{margin:0;padding:0;box-sizing:border-box;}
  html,body{width:1200px;height:851px;overflow:hidden;background:var(--stage);font-family:var(--body-font);}
  .page{position:absolute;top:101px;width:445px;height:630px;background:var(--white);overflow:hidden;}
  .page--front{left:154px;}
  .page--back{left:638px;}
  .page svg.shapes{position:absolute;inset:0;}
  p{hyphens:auto;-webkit-hyphens:auto;}

  .brand{position:absolute;display:flex;align-items:center;gap:7px;color:var(--white);font-weight:600;letter-spacing:.3px;white-space:nowrap;}
  .brand__dot{width:20px;height:20px;border-radius:50%;background:linear-gradient(135deg,var(--purple),var(--cyan));flex:none;}
  .page--front .brand{left:26px;top:31px;font-size:15px;}
  .page--back .brand{left:28px;top:567px;font-size:13px;}

  .badge{position:absolute;left:32px;top:79px;width:138px;height:138px;border-radius:50%;
    background:linear-gradient(160deg,var(--purple) 0%,#7f5cf0 50%,var(--cyan) 100%);
    border:3px solid var(--white);display:flex;align-items:center;justify-content:center;text-align:center;
    color:var(--white);font-weight:700;font-size:14.5px;line-height:17px;text-transform:uppercase;}

  .specialize{position:absolute;left:172px;width:222px;top:296px;text-align:center;color:var(--white);}
  .specialize__title{font-family:var(--script-font);font-weight:400;font-size:30px;line-height:34px;margin-bottom:4px;}
  .specialize p{font-size:8.6px;line-height:10.9px;margin-bottom:10.5px;}

  .contact-front{position:absolute;left:28px;top:558px;}
  .contact-front__label{font-weight:700;font-size:12px;line-height:13px;color:var(--ink);}
  .phone{font-weight:700;background:linear-gradient(90deg,var(--purple),var(--blue) 55%,var(--cyan));
    -webkit-background-clip:text;background-clip:text;color:transparent;letter-spacing:-.3px;white-space:nowrap;}
  .contact-front .phone{font-size:24px;line-height:26px;}
  .web{display:inline-block;border-radius:8px;font-size:7.4px;letter-spacing:1.6px;text-align:center;}
  .web b{font-weight:700;}
  .contact-front .web{background:var(--black);color:var(--white);width:156px;padding:1px 0;}

  .intro-card{position:absolute;left:14px;top:14px;width:419px;height:278px;border-radius:10px;
    background:linear-gradient(100deg,var(--purple) 0%,#8b4ff0 45%,#2d8af2 85%,var(--cyan) 100%);
    box-shadow:0 4px 6px rgba(0,0,0,.25);color:var(--white);}
  .intro-card__photo{position:absolute;left:14px;top:14px;width:162px;height:157px;
    background:linear-gradient(135deg,#e8eef5,#c9d6e4 55%,#9a7a64);}
  .intro-card__lead{position:absolute;left:192px;top:11px;width:214px;font-size:8.4px;line-height:10.8px;text-align:justify;letter-spacing:-.05px;}
  .intro-card__plan{position:absolute;left:14px;top:187px;width:392px;font-size:8.4px;line-height:10.8px;text-align:justify;letter-spacing:-.05px;}

  .doctor-photo{position:absolute;left:19px;top:320px;width:126px;height:126px;border-radius:50%;
    background:radial-gradient(circle at 50% 40%,#d9d9d9,#7a7a7a 70%,#3a3a3a);}
  .doctor-bio{position:absolute;left:158px;top:315px;width:240px;font-size:8px;line-height:9.9px;color:var(--ink);text-align:justify;}
  .doctor-bio b{font-weight:700;}

  .contact-back{position:absolute;right:30px;top:536px;text-align:right;}
  .contact-back__label{color:var(--white);font-weight:700;font-size:13px;line-height:15px;}
  .contact-back .phone{font-size:32px;line-height:36px;}
  .contact-back .web{background:var(--white);color:var(--ink);width:224px;font-size:9px;padding:1px 0;border-radius:9px;}
</style>
</head>
<body>

<section class="page page--front">
  <svg class="shapes" viewBox="0 0 445 630" width="445" height="630">
    <defs>
      <linearGradient id="heroGrad" x1="0" y1="0" x2="1" y2="1">
        <stop offset="0" stop-color="#5b4a3c"/><stop offset=".5" stop-color="#a2866c"/><stop offset="1" stop-color="#d8d4cc"/>
      </linearGradient>
      <linearGradient id="specialtyGrad" x1="0" y1="0" x2="1" y2="1">
        <stop offset="0" stop-color="#7a3bdc"/><stop offset=".5" stop-color="#3a2aa8"/><stop offset="1" stop-color="#1947b8"/>
      </linearGradient>
      <linearGradient id="edgeGrad" x1="0" y1="0" x2="1" y2="0">
        <stop offset="0" stop-color="#a63ee6"/><stop offset="1" stop-color="#2f5fe0"/>
      </linearGradient>
    </defs>
    <rect x="0" y="0" width="445" height="280" fill="url(#heroGrad)" role="img" aria-label="Photo of a therapist and a client talking in a bright lounge"/>
    <path d="M0 0 H232 C212 100 140 170 0 198 Z" fill="var(--black)"/>
    <path d="M232 0 C212 100 140 170 0 198" fill="none" stroke="var(--cyan)" stroke-width="6"/>
    <path d="M0 198 C60 186 110 168 150 150 C170 200 260 225 445 252 V630 H0 Z" fill="var(--white)"/>
    <path d="M0 292 C110 240 290 210 445 262 V630 H0 Z" fill="url(#specialtyGrad)" role="img" aria-label="Illustration of a woman's profile with a glowing digital brain"/>
    <path d="M0 292 C110 240 290 210 445 262" fill="none" stroke="var(--black)" stroke-width="3"/>
    <path d="M0 552 C110 532 230 560 300 630 H0 Z" fill="var(--white)"/>
    <path d="M0 552 C110 532 230 560 300 630" fill="none" stroke="url(#edgeGrad)" stroke-width="5"/>
  </svg>

  <div class="brand"><span class="brand__dot"></span>Varnel Psychiatry</div>

  <div class="badge">Is now<br>accepting<br>new patients<br>in Boulder<br>Colorado!</div>

  <div class="specialize">
    <h2 class="specialize__title">We specialize in :</h2>
    <p>treating patients with treatment resistant depression and substance abuse disorders who have not responded to other forms of treatment. We also treat patients with PTSD, Bipolar Disorder, OCD, anxiety disorders, ADHD, and psychotic disorders. We believe that by providing comprehensive care, we can help our patients heal both emotionally and physically.</p>
    <p>We know that mental health is complex and that multiple factors can contribute to the development of mental illness. For this reason, we take an integrative approach that considers the whole person. We understand that each individual has their own unique set of experiences, strengths, and challenges, and we tailor our treatment plans to suit each patient’s personal needs.</p>
  </div>

  <div class="contact-front">
    <div class="contact-front__label">CALL US TODAY:</div>
    <div class="phone">555.014.2286</div>
    <div class="web">WWW.<b>VARNELPSYCHIATRY</b>.COM</div>
  </div>
</section>

<section class="page page--back">
  <svg class="shapes" viewBox="0 0 445 630" width="445" height="630">
    <defs>
      <radialGradient id="haloGrad" cx=".35" cy=".5" r=".65">
        <stop offset="0" stop-color="#d8cdfb"/><stop offset=".7" stop-color="#e9e4fd"/><stop offset="1" stop-color="#ffffff" stop-opacity="0"/>
      </radialGradient>
      <linearGradient id="backEdgeGrad" x1="0" y1="0" x2="1" y2="0">
        <stop offset="0" stop-color="#a63ee6"/><stop offset=".6" stop-color="#6a3bd8"/><stop offset="1" stop-color="#2f5fe0"/>
      </linearGradient>
    </defs>
    <ellipse cx="150" cy="390" rx="160" ry="120" fill="url(#haloGrad)"/>
    <path d="M0 462 C90 530 260 540 445 436 V630 H0 Z" fill="var(--black)"/>
    <path d="M0 462 C90 530 260 540 445 436" fill="none" stroke="url(#backEdgeGrad)" stroke-width="5"/>
  </svg>

  <div class="intro-card">
    <div class="intro-card__photo" role="img" aria-label="Photo of a patient receiving transcranial magnetic stimulation beside the device"></div>
    <p class="intro-card__lead">So often, when we think about mental health, we focus on just treating symptoms. If someone is depressed, they might take medication to help them feel better. If someone is anxious, they might see a therapist to help them manage their anxiety. While these treatments can be helpful, they only address the symptoms of mental illness. To truly address mental health, it is necessary to treat the root causes. This might involve addressing childhood trauma, unresolved conflict, or feelings of worthlessness. It might also involve developing healthy coping mechanisms and learning how to set boundaries. By treating the root causes of mental illness, we can begin to create lasting change.</p>
    <p class="intro-card__plan">Our personalized psychiatry plan includes a bio-psycho-social evaluation, tailored treatment plan, medical evaluation for underlying hormonal and electrolyte abnormalities, and genetic testing (when warranted). Our integrative psychiatry approach combines cutting edge, evidence-based treatments with holistic therapies to provide you with the best possible care. In addition, we also offer Ketamine Assisted Therapy, TMS (Transcranial Magnetic Simulation), and MAT Treatment for Substance abuse. We pride ourselves on always staying up to date on the latest mental health treatments.</p>
  </div>

  <div class="doctor-photo" role="img" aria-label="Black and white portrait of Dr. Tomas Brok"></div>
  <p class="doctor-bio"><b>Dr. Tomas Brok</b> is a psychiatrist with years of experience providing compassionate, evidence-based care to patients of all ages. He is uniquely trained in several cutting-edge treatments, including Ketamine, Transcranial Magnetic Stimulation (TMS), and integrative psychiatry. Prior to founding Varnel Psychiatry, Dr. Brok served as Chief Resident at the largest private psychiatry hospital in Colorado. While there, he won three consecutive awards for exceptionally high Psychiatry in-service test scores (99th percentile). In addition, he was a board member of the Kestrel Mind Guild and helped advocate for better Colorado mental health policy. Thanks to his extensive training and experience, Dr. Brok is able to provide each patient with an individualized treatment plan that brings optimum results.</p>

  <div class="brand"><span class="brand__dot"></span>Varnel Psychiatry</div>

  <div class="contact-back">
    <div class="contact-back__label">CALL US TODAY</div>
    <div class="phone">555.014.2286</div>
    <div class="web">WWW.<b>VARNELPSYCHIATRY</b>.COM</div>
  </div>
</section>

</body>
</html>
```